Arvo 7 Detection Wheel

We need a professional **framework wheel diagram** designed for our detection dog training manual.

Our business is **Arvo 7 Dog Training**, and this graphic represents our **Detection Training Model**.

Please use the **attached reference images** as a guide for the structure and layout of the wheel.

### What we need

1. **Full wheel graphic**

* Clean circular framework wheel
* Similar structure to the attached example
* Clear sections and text
* Professional training manual style
* Transparent background

2. **Individual segment pieces**

We also need the **inner sections broken into separate pieces** (like the second reference image).

This will allow us to place each section on different pages of the manual when explaining the concepts.

Each piece should look like a **slice of the wheel**.

### Style

The design should look:

• Professional
• Clean and modern
• Structured and easy to read
• Suitable for a training manual

Avoid cartoon styles or clipart.

### Colours

Please use our brand colour palette (see attached image):

* Dark navy blue
* Steel blue
* Light blue
* White
* Light grey
* Dark grey

### Files required

Final files must include:

* Vector files (AI or EPS)
* Transparent PNG
* High-resolution PDF

Please also provide **each segment exported individually**

```html
<!DOCTYPE html>
<html lang="en">
<head>
<meta charset="utf-8">
<title>Arvo 7 Detection Wheel</title>
<link rel="stylesheet" href="https://fonts.googleapis.com/css2?family=Montserrat:wght@700&display=swap">
<style>
  :root {
    --navy-deep: #0b2357;
    --navy: #123a7a;
    --steel: #1d4f9a;
    --sky: #1ea7e6;
    --white: #ffffff;
    --paper: #ffffff;
  }
  html, body {
    margin: 0;
    padding: 0;
    width: 1200px;
    height: 1200px;
    overflow: hidden;
    background: var(--paper);
  }
  .wheel-canvas {
    width: 1200px;
    height: 1200px;
    display: block;
  }
  .wheel-slice {
    fill: url(#slice-fill);
    stroke: var(--sky);
    stroke-width: 4;
    stroke-linejoin: miter;
  }
  .slice-label {
    font-family: "Montserrat", Arial, sans-serif;
    font-weight: 700;
    font-size: 22px;
    letter-spacing: 0.6px;
    fill: var(--white);
  }
</style>
</head>
<body>
<svg class="wheel-canvas" viewBox="0 0 1040 1040" role="img" aria-label="Detection Training Model half wheel with five segments">
  <defs>
    <linearGradient id="slice-fill" x1="0" y1="0" x2="1" y2="1">
      <stop offset="0" stop-color="var(--steel)"/>
      <stop offset="0.45" stop-color="var(--navy)"/>
      <stop offset="1" stop-color="var(--navy-deep)"/>
    </linearGradient>
  </defs>

  <g class="segment segment-generic-suitability">
    <path class="wheel-slice" d="M400,665 L97,665 A304,304 0 0 1 158,481 Z"/>
    <text class="slice-label" x="152" y="616">GENERIC</text>
    <text class="slice-label" x="152" y="644">SUITABILITY</text>
  </g>

  <g class="segment segment-health">
    <path class="wheel-slice" d="M452,665 L180,453 A345,345 0 0 1 370,330 Z"/>
    <text class="slice-label" x="245" y="443">HEALTH &amp;</text>
    <text class="slice-label" x="245" y="472">PHYSICAL</text>
    <text class="slice-label" x="245" y="501">WELLBEING</text>
  </g>

  <g class="segment segment-engagement">
    <path class="wheel-slice" d="M488,665 L397,268 A407,407 0 0 1 661,296 Z"/>
    <text class="slice-label" x="430" y="345">ENGAGEMENT</text>
    <text class="slice-label" x="430" y="374">RELATIONSHIP</text>
  </g>

  <g class="segment segment-reward">
    <path class="wheel-slice" d="M522,670 L705,285 A426,426 0 0 1 886,446 Z"/>
    <text class="slice-label" x="687" y="443">REWARD</text>
    <text class="slice-label" x="687" y="472">VALUE</text>
  </g>

  <g class="segment segment-arousal">
    <path class="wheel-slice" d="M585,663 L885,483 A351,351 0 0 1 937,662 Z"/>
    <text class="slice-label" x="720" y="614">AROUSAL</text>
    <text class="slice-label" x="720" y="643">REGULATION</text>
  </g>
</svg>
</body>
</html>
```